The Bayfield Wellness Clinic - Practice Flyer

We need a flyer that generally advertises our services. I've uploaded one old flyer as well as examples of others. I like the style of the materials made by this practice: https://www.facebook.com/PineRidgeCounselingHouse

```html
<!DOCTYPE html>
<html lang="en">
<head>
<meta charset="utf-8">
<title>The Bayfield Wellness Clinic – Practice Flyer</title>
<link rel="stylesheet" href="https://fonts.googleapis.com/css2?family=Playfair+Display:wght@400;700&family=Cabin:wght@400;600&family=Roboto:wght@500;700&display=swap">
<style>
  :root {
    --forest: #3b4834;
    --lime: #a9c23f;
    --olive: #8f8c4c;
    --green: #4b8b3b;
    --green-deep: #3f7d33;
    --ink: #2b2b2b;
    --pale: #eef3e3;
    --white: #ffffff;
  }
  * { margin: 0; padding: 0; box-sizing: border-box; }
  html, body { width: 990px; height: 1200px; overflow: hidden; background: #dcdcdc; }
  .flyer { position: relative; width: 990px; height: 1200px; overflow: hidden;
    background: linear-gradient(180deg, #f6f7f4 0%, var(--pale) 55%, #e6eedb 100%);
    font-family: "Cabin", sans-serif; color: var(--ink); }
  .backdrop { position: absolute; inset: 0; }
  .brand { position: absolute; top: 78px; left: 0; width: 990px; text-align: center;
    font-family: "Playfair Display", serif; font-weight: 700; font-size: 44px;
    color: var(--olive); letter-spacing: 1px; }
  .headline { position: absolute; top: 520px; left: 60px; width: 870px; text-align: center;
    font-family: "Playfair Display", serif; font-weight: 700; font-size: 25px; line-height: 32px; }
  .headline .accent { color: var(--green); }
  .col { position: absolute; top: 665px; font-size: 14px; line-height: 18.5px; }
  .col-left { left: 78px; width: 380px; }
  .col-right { left: 462px; width: 400px; }
  .col .accent { color: var(--green); font-weight: 600; }
  .divider { position: absolute; top: 738px; left: 118px; width: 314px; height: 1px; background: var(--green); }
  .divider-dot { position: absolute; top: 731px; left: 94px; width: 14px; height: 14px; border-radius: 50%; background: var(--lime); }
  .checklist { position: absolute; list-style: none; font-size: 13.5px; }
  .checklist li { display: flex; align-items: center; gap: 7px; }
  .checklist svg { flex: none; }
  .conditions { top: 750px; left: 78px; }
  .conditions li { height: 20.2px; }
  .treatments { top: 781px; left: 462px; }
  .treatments li { height: 22.6px; }
  .section-tab { position: absolute; top: 740px; left: 462px; width: 389px; height: 33px;
    background: var(--green); color: var(--white); font-family: "Roboto", sans-serif;
    font-weight: 700; font-size: 20px; line-height: 33px; padding-left: 27px; border-radius: 2px; }
  .clinician-tab { position: absolute; top: 940px; left: 78px; width: 283px; height: 33px;
    background: var(--green); color: var(--white); font-family: "Playfair Display", serif;
    font-weight: 700; font-size: 21px; line-height: 33px; padding-left: 24px; border-radius: 2px; }
  .credentials { position: absolute; top: 983px; left: 78px; padding-left: 12px;
    border-left: 2px solid var(--green); font-family: "Roboto", sans-serif; font-weight: 500;
    font-size: 14px; line-height: 21.5px; }
  .credentials .accent { color: var(--green); }
  .phone { position: absolute; top: 959px; left: 464px; width: 369px; height: 49px;
    background: var(--green); border-radius: 25px; }
  .phone-badge { position: absolute; left: -2px; top: -4px; width: 57px; height: 57px;
    border-radius: 50%; background: var(--white); border: 5px solid var(--lime);
    display: flex; align-items: center; justify-content: center; }
  .phone-number { position: absolute; left: 76px; top: 0; line-height: 49px;
    font-family: "Roboto", sans-serif; font-weight: 700; font-size: 34px; color: var(--white); }
  .website { position: absolute; top: 1130px; left: 80px; font-family: "Playfair Display", serif;
    font-size: 25px; color: var(--white); }
  .website b { font-weight: 700; }
  .website .accent { color: var(--lime); font-weight: 400; }
  .footer-rule { position: absolute; top: 1133px; left: 640px; width: 2px; height: 24px; background: var(--white); }
  .social { position: absolute; top: 1132px; left: 667px; display: flex; gap: 12px; }
  .social span { width: 32px; height: 32px; border-radius: 50%; background: var(--white); }
</style>
</head>
<body>
<div class="flyer">
  <svg class="backdrop" width="990" height="1200" viewBox="0 0 990 1200">
    <defs>
      <linearGradient id="lakeScene" x1="0" y1="0" x2="0" y2="1">
        <stop offset="0" stop-color="#f4f4f2"/>
        <stop offset="0.35" stop-color="#8d918c"/>
        <stop offset="0.6" stop-color="#3c4433"/>
        <stop offset="0.8" stop-color="#6e726c"/>
        <stop offset="1" stop-color="#9a9c97"/>
      </linearGradient>
      <linearGradient id="portraitWarm" x1="0" y1="0" x2="1" y2="1">
        <stop offset="0" stop-color="#d8c1a6"/>
        <stop offset="0.6" stop-color="#9d4a3e"/>
        <stop offset="1" stop-color="#6d4a3a"/>
      </linearGradient>
      <linearGradient id="portraitCool" x1="0" y1="0" x2="1" y2="1">
        <stop offset="0" stop-color="#e6eef2"/>
        <stop offset="1" stop-color="#7f9fb2"/>
      </linearGradient>
    </defs>
    <path role="img" aria-label="Misty mountain lake with forested shores" fill="url(#lakeScene)"
      d="M0,180 H990 V505 C930,440 870,400 800,380 L560,405 C420,440 300,470 200,440 C120,415 60,390 0,360 Z"/>
    <path fill="var(--lime)" d="M0,358 C70,400 140,430 230,445 C340,462 450,440 560,405 L575,420 C460,468 340,488 220,470 C130,455 60,420 0,395 Z"/>
    <path fill="var(--forest)" d="M130,410 C200,455 280,475 400,468 C470,463 520,448 570,430 L575,452 C500,485 420,505 330,503 C250,500 180,470 130,410 Z"/>
    <path fill="var(--lime)" d="M800,385 C880,410 950,460 990,505 V530 C940,480 880,440 800,410 Z"/>
    <path fill="var(--forest)" d="M860,420 C920,445 960,475 990,500 V512 C950,475 905,445 860,420 Z"/>
    <circle cx="692" cy="378" r="136" fill="var(--white)"/>
    <circle role="img" aria-label="Portrait of a stressed woman at a desk with coffee" cx="692" cy="378" r="129" fill="url(#portraitWarm)"/>
    <circle cx="524" cy="419" r="90" fill="var(--white)"/>
    <circle role="img" aria-label="Portrait of a man holding his head in worry" cx="524" cy="419" r="84" fill="url(#portraitCool)"/>
    <path fill="var(--lime)" d="M0,1003 C120,1060 260,1085 420,1068 C600,1048 780,1030 900,1080 C940,1098 970,1120 990,1140 V1170 C900,1090 760,1070 600,1085 C420,1102 220,1120 0,1060 Z"/>
    <path fill="var(--forest)" d="M0,1040 C150,1110 320,1118 480,1100 C640,1082 800,1070 900,1110 C940,1130 970,1150 990,1170 V1200 H0 Z"/>
  </svg>

  <div class="brand">The Bayfield Wellness Clinic</div>

  <p class="headline"><span class="accent">The Bayfield Wellness Clinic</span> of Greater Philadelphia, (BWC) provides expert clinical care for <span class="accent">anxiety disorders, obsessive compulsive and related disorders,</span> and <span class="accent">neurodevelopmental disorders</span> in children, adolescents, and adults.</p>

  <p class="col col-left"><span class="accent">BWC</span> proudly provides the Greater Philadelphia community with state-of-the-art assessment and evidence-based therapy for disorders including:</p>
  <p class="col col-right"><span class="accent">BWC</span> clinicians are highly trained in <span class="accent">cognitive behavioral therapy (CBT),</span> which includes scientifically informed techniques that are tailored to each client's unique needs.</p>

  <div class="divider-dot"></div>
  <div class="divider"></div>

  <ul class="checklist conditions">
    <li><svg width="11" height="11" viewBox="0 0 12 12"><circle cx="6" cy="6" r="5.2" fill="none" stroke="var(--green)" stroke-width="1"/><path d="M3.6,6.2 L5.3,7.8 L8.5,4.4" fill="none" stroke="var(--green)" stroke-width="1.1"/></svg>Obsessive Compulsive Disorder</li>
    <li><svg width="11" height="11" viewBox="0 0 12 12"><circle cx="6" cy="6" r="5.2" fill="none" stroke="var(--green)" stroke-width="1"/><path d="M3.6,6.2 L5.3,7.8 L8.5,4.4" fill="none" stroke="var(--green)" stroke-width="1.1"/></svg>Trichotillomania Excoriation Disorder</li>
    <li><svg width="11" height="11" viewBox="0 0 12 12"><circle cx="6" cy="6" r="5.2" fill="none" stroke="var(--green)" stroke-width="1"/><path d="M3.6,6.2 L5.3,7.8 L8.5,4.4" fill="none" stroke="var(--green)" stroke-width="1.1"/></svg>Generalized Anxiety Disorder Panic Disorder</li>
    <li><svg width="11" height="11" viewBox="0 0 12 12"><circle cx="6" cy="6" r="5.2" fill="none" stroke="var(--green)" stroke-width="1"/><path d="M3.6,6.2 L5.3,7.8 L8.5,4.4" fill="none" stroke="var(--green)" stroke-width="1.1"/></svg>Specific Phobias</li>
    <li><svg width="11" height="11" viewBox="0 0 12 12"><circle cx="6" cy="6" r="5.2" fill="none" stroke="var(--green)" stroke-width="1"/><path d="M3.6,6.2 L5.3,7.8 L8.5,4.4" fill="none" stroke="var(--green)" stroke-width="1.1"/></svg>Hoarding Disorder Body Dysmorphic Disorder</li>
    <li><svg width="11" height="11" viewBox="0 0 12 12"><circle cx="6" cy="6" r="5.2" fill="none" stroke="var(--green)" stroke-width="1"/><path d="M3.6,6.2 L5.3,7.8 L8.5,4.4" fill="none" stroke="var(--green)" stroke-width="1.1"/></svg>Tic Disorders</li>
    <li><svg width="11" height="11" viewBox="0 0 12 12"><circle cx="6" cy="6" r="5.2" fill="none" stroke="var(--green)" stroke-width="1"/><path d="M3.6,6.2 L5.3,7.8 L8.5,4.4" fill="none" stroke="var(--green)" stroke-width="1.1"/></svg>ADHD Learning Disorders</li>
    <li><svg width="11" height="11" viewBox="0 0 12 12"><circle cx="6" cy="6" r="5.2" fill="none" stroke="var(--green)" stroke-width="1"/><path d="M3.6,6.2 L5.3,7.8 L8.5,4.4" fill="none" stroke="var(--green)" stroke-width="1.1"/></svg>Insomnia</li>
    <li><svg width="11" height="11" viewBox="0 0 12 12"><circle cx="6" cy="6" r="5.2" fill="none" stroke="var(--green)" stroke-width="1"/><path d="M3.6,6.2 L5.3,7.8 L8.5,4.4" fill="none" stroke="var(--green)" stroke-width="1.1"/></svg>Social Anxiety Disorder</li>
  </ul>

  <div class="section-tab">Treatments We Provide:</div>
  <ul class="checklist treatments">
    <li><svg width="11" height="11" viewBox="0 0 12 12"><circle cx="6" cy="6" r="5.2" fill="none" stroke="var(--green)" stroke-width="1"/><path d="M3.6,6.2 L5.3,7.8 L8.5,4.4" fill="none" stroke="var(--green)" stroke-width="1.1"/></svg>Cognitive Behavioral Therapy (CBT)</li>
    <li><svg width="11" height="11" viewBox="0 0 12 12"><circle cx="6" cy="6" r="5.2" fill="none" stroke="var(--green)" stroke-width="1"/><path d="M3.6,6.2 L5.3,7.8 L8.5,4.4" fill="none" stroke="var(--green)" stroke-width="1.1"/></svg>Exposure and Response Prevention (E/RP)</li>
    <li><svg width="11" height="11" viewBox="0 0 12 12"><circle cx="6" cy="6" r="5.2" fill="none" stroke="var(--green)" stroke-width="1"/><path d="M3.6,6.2 L5.3,7.8 L8.5,4.4" fill="none" stroke="var(--green)" stroke-width="1.1"/></svg>Comprehensive Behavioral (ComB)/Habit Reversal Training (HRT)</li>
    <li><svg width="11" height="11" viewBox="0 0 12 12"><circle cx="6" cy="6" r="5.2" fill="none" stroke="var(--green)" stroke-width="1"/><path d="M3.6,6.2 L5.3,7.8 L8.5,4.4" fill="none" stroke="var(--green)" stroke-width="1.1"/></svg>Cognitive Behavioral Intervention for Tics (CBIT)</li>
    <li><svg width="11" height="11" viewBox="0 0 12 12"><circle cx="6" cy="6" r="5.2" fill="none" stroke="var(--green)" stroke-width="1"/><path d="M3.6,6.2 L5.3,7.8 L8.5,4.4" fill="none" stroke="var(--green)" stroke-width="1.1"/></svg>Acceptance and Commitment Therapy (ACT)</li>
    <li><svg width="11" height="11" viewBox="0 0 12 12"><circle cx="6" cy="6" r="5.2" fill="none" stroke="var(--green)" stroke-width="1"/><path d="M3.6,6.2 L5.3,7.8 L8.5,4.4" fill="none" stroke="var(--green)" stroke-width="1.1"/></svg>Organizational Skills Training (OST)</li>
    <li><svg width="11" height="11" viewBox="0 0 12 12"><circle cx="6" cy="6" r="5.2" fill="none" stroke="var(--green)" stroke-width="1"/><path d="M3.6,6.2 L5.3,7.8 L8.5,4.4" fill="none" stroke="var(--green)" stroke-width="1.1"/></svg>CBT for Insomnia (CBT-I)</li>
  </ul>

  <div class="clinician-tab">Helena R. Marsh, PsyD</div>
  <div class="credentials">
    <div>Executive Director Licensed Clinical Psychologist</div>
    <div><span class="accent">New Jersey Lic. No.</span> 35S20871146</div>
    <div><span class="accent">Pennsylvania Lic. No.</span> Ps0482315</div>
  </div>

  <div class="phone">
    <div class="phone-badge">
      <svg width="26" height="26" viewBox="0 0 24 24"><path fill="var(--green)" d="M6.6,10.8 C8,13.6 10.4,16 13.2,17.4 L15.4,15.2 C15.7,14.9 16.1,14.8 16.4,15 C17.5,15.4 18.7,15.6 20,15.6 C20.6,15.6 21,16 21,16.6 V20 C21,20.6 20.6,21 20,21 C10.6,21 3,13.4 3,4 C3,3.4 3.4,3 4,3 H7.5 C8.1,3 8.5,3.4 8.5,4 C8.5,5.3 8.7,6.5 9.1,7.6 C9.2,7.9 9.1,8.3 8.9,8.6 Z"/></svg>
    </div>
    <div class="phone-number">(555) 014-2837</div>
  </div>

  <div class="website">www.<b>TheBayfield</b><span class="accent">Wellness</span><b>Clinic</b>.com</div>
  <div class="footer-rule"></div>
  <div class="social" aria-label="Social media links"><span></span><span></span><span></span><span></span></div>
</div>
</body>
</html>
```